Photo booth placards - Customers select after a game for a fun group photo

i am wanting 24 photobooth placards to fit on a peice of corflute (2400 x 1220) all on one file to print. Must be Bright and fun, each one different style /colour.
Escape room placards- approx. A3(file size with all on the one file 2400 x 1220) Require as a source file and high res pdf.
1. Photo Booth - Grab a prop and strike a post (this one is for the box that will contain the other signs)
2. Photo Booth - Grab a prop and strike a post (this one is for the box that will contain the other signs)
3. GENIUS
4. Nailed it!
5. I’m Awesome
6. We escaped
7. (arrow left) They were no help (Arrow Right)
8. We did it!
9. I’m still confused??
10. They Should have listened to me
11. Weakest link (arrow)
12. I’m the smart one
13. Escape Artist
14. I did EVERYTHING
15. Winners
16. No one listens to me
17. I survived by my wits (and good looks)
18. Escaped in time - woohoo!
19. We ALMOST beat the clock
20. (arrow left) Genius – We Escaped- Sidekick (arrow right)
21. We suck
22. I’m glad they’re smart
23. Mission completed
24. I’m with stupid (arrow)

some sample ideas attached...

```html
<!DOCTYPE html>
<html lang="en">
<head>
<meta charset="utf-8">
<title>Photo Booth Placards</title>
<link rel="stylesheet" href="https://fonts.googleapis.com/css2?family=Cabin+Sketch:wght@700&family=League+Gothic&family=Yellowtail&family=Lobster&family=Archivo+Black&family=Alfa+Slab+One&display=swap">
<style>
  :root {
    --page: #ffffff;
    --chalk-frame: #c0975a;
    --chalk-green: #3d7a47;
    --chalk-white: #eef2ea;
    --ink-black: #000000;
    --link-yellow: #f2c200;
    --dart-red: #e0282e;
    --board-grey: #3a3a3a;
    --sunny: #ffcc00;
    --smart-navy: #13309a;
    --bulb-glow: #ffe066;
    --clock-navy: #0f5078;
    --clock-red: #df4350;
    --burst-white: #fbfbfd;
    --stupid-gold: #d9a810;
    --stupid-border: #3a3a3a;
  }
  html, body {
    margin: 0;
    padding: 0;
    width: 1200px;
    height: 1200px;
    overflow: hidden;
    background: var(--page);
  }
  .sheet {
    position: relative;
    width: 1200px;
    height: 1200px;
  }
  .placard {
    position: absolute;
    width: 516px;
    height: 262px;
    display: block;
  }
  .col-left { left: 73px; }
  .col-right { left: 612px; }
  .row-top { top: 187px; }
  .row-mid-left { top: 465px; }
  .row-mid-right { top: 461px; }
  .row-bottom { top: 753px; }

  .genius-word { font-family: "Cabin Sketch", cursive; font-weight: 700; fill: var(--chalk-white); }
  .chalk-note { font-family: "Cabin Sketch", cursive; fill: var(--chalk-white); }
  .link-word { font-family: "League Gothic", sans-serif; fill: #ffffff; }
  .nailed-word { font-family: "Yellowtail", cursive; fill: var(--dart-red); stroke: #ffffff; stroke-width: 3; paint-order: stroke; }
  .smart-word { font-family: "Lobster", cursive; fill: var(--smart-navy); }
  .clock-red-word { font-family: "Archivo Black", sans-serif; fill: var(--clock-red); }
  .clock-navy-word { font-family: "Archivo Black", sans-serif; fill: var(--clock-navy); }
  .stupid-word { font-family: "Alfa Slab One", serif; fill: var(--ink-black); font-style: italic; }
</style>
</head>
<body>
<main class="sheet">

  <!-- GENIUS chalkboard -->
  <svg class="placard col-left row-top" viewBox="0 0 645 327">
    <rect class="chalk-frame" width="645" height="327" fill="var(--chalk-frame)"/>
    <rect class="chalk-board" x="16" y="14" width="613" height="298" fill="var(--chalk-green)"/>
    <text class="genius-word" x="349" y="210" font-size="118" text-anchor="middle">GENIUS!</text>
    <text class="chalk-note" x="112" y="262" font-size="26">e=mc²</text>
    <text class="chalk-note" x="282" y="68" font-size="30">@</text>
    <text class="chalk-note" x="488" y="262" font-size="26">@</text>
    <text class="chalk-note" x="78" y="285" font-size="56" transform="rotate(-12 90 260)">!</text>
  </svg>

  <!-- WEAKEST LINK -->
  <svg class="placard col-right row-top" viewBox="0 0 645 327">
    <rect width="645" height="327" fill="var(--ink-black)"/>
    <text class="link-word" x="30" y="212" font-size="150" textLength="350" lengthAdjust="spacingAndGlyphs">WEAKEST</text>
    <rect role="img" aria-label="Broken chain link illustration" x="378" y="132" width="112" height="36" rx="18" fill="var(--link-yellow)"/>
    <text class="link-word" x="445" y="212" font-size="150" textLength="178" lengthAdjust="spacingAndGlyphs">LINK</text>
    <line x1="215" y1="260" x2="498" y2="260" stroke="var(--link-yellow)" stroke-width="8"/>
    <polygon points="142,260 226,232 218,260 226,292" fill="var(--link-yellow)"/>
  </svg>

  <!-- NAILED IT -->
  <svg class="placard col-left row-mid-left" viewBox="0 0 645 327">
    <rect width="645" height="327" fill="var(--ink-black)"/>
    <rect x="20" y="18" width="605" height="291" fill="none" stroke="#ffffff" stroke-width="3"/>
    <circle cx="322" cy="164" r="152" fill="#ffffff"/>
    <circle role="img" aria-label="Dartboard illustration" cx="322" cy="164" r="144" fill="var(--board-grey)"/>
    <text class="nailed-word" x="322" y="205" font-size="128" text-anchor="middle" transform="rotate(-6 322 170)">Nailed it</text>
  </svg>

  <!-- I'M THE SMART ONE -->
  <svg class="placard col-right row-mid-right" viewBox="0 0 645 327">
    <rect width="645" height="327" fill="var(--sunny)"/>
    <path d="M70,60 C140,30 200,55 260,40 C340,20 420,55 500,40 C560,28 600,20 610,40 C590,80 640,120 600,170 C570,215 640,240 615,265 C560,300 480,290 420,300 C340,312 280,285 220,300 C150,315 90,300 40,260 C20,240 60,200 45,160 C30,120 40,80 70,60 Z" fill="#ffffff"/>
    <text class="smart-word" x="70" y="140" font-size="62" transform="rotate(-3 320 120)">I’m the smart one</text>
    <circle role="img" aria-label="Light bulb icon" cx="330" cy="200" r="44" fill="var(--bulb-glow)" stroke="var(--smart-navy)" stroke-width="5"/>
  </svg>

  <!-- WE ALMOST BEAT THE CLOCK -->
  <svg class="placard col-left row-bottom" viewBox="0 0 645 327">
    <rect width="645" height="327" fill="var(--clock-navy)"/>
    <polygon fill="var(--burst-white)" points="55,0 170,45 225,0 300,60 380,0 460,45 560,0 585,60 645,70 605,130 645,200 600,240 640,310 520,290 470,327 380,285 300,327 240,280 160,327 110,270 40,305 50,230 0,195 40,135 0,95 45,60"/>
    <text class="clock-red-word" x="75" y="102" font-size="42">WE</text>
    <text class="clock-navy-word" x="72" y="188" font-size="100" textLength="510" lengthAdjust="spacingAndGlyphs">ALMOST</text>
    <circle role="img" aria-label="Ringing alarm clock illustration" cx="390" cy="148" r="52" fill="#ffffff" stroke="var(--clock-navy)" stroke-width="9"/>
    <text class="clock-red-word" x="75" y="248" font-size="44" textLength="500" lengthAdjust="spacingAndGlyphs">BEAT THE CLOCK</text>
  </svg>

  <!-- I'M WITH STUPID -->
  <svg class="placard col-right row-bottom" viewBox="0 0 645 327">
    <rect width="645" height="327" fill="var(--stupid-gold)"/>
    <rect x="38" y="29" width="570" height="270" fill="none" stroke="var(--stupid-border)" stroke-width="6"/>
    <text class="stupid-word" x="322" y="155" font-size="52" text-anchor="middle">I’m with Stupid</text>
    <line x1="215" y1="216" x2="495" y2="216" stroke="var(--ink-black)" stroke-width="6"/>
    <polygon points="138,216 228,190 218,216 228,248" fill="var(--ink-black)"/>
  </svg>

</main>
</body>
</html>
```